Velmont Chamber of Commerce Website

We have been asked to design a new website for the Velmont Chamber of Commerce. The mission of the Greater Velmont Chamber of Commerce is to develop and promote an economically vibrant business community aggressively. The website should reflect a modern, professional design that showcases local businesses and promotes the programs the Chamber has to offer.

```html
<!DOCTYPE html>
<html lang="en">
<head>
<meta charset="utf-8">
<title>Greater Velmont Chamber of Commerce</title>
<link href="https://fonts.googleapis.com/css2?family=Roboto:wght@400;500;700;900&family=Poppins:wght@400;500&display=swap" rel="stylesheet">
<style>
:root{
  --navy:#1d3768;
  --navy-deep:#1a3263;
  --blue:#2f5fa7;
  --light:#f2f2f2;
  --ink:#1b1b1b;
  --white:#ffffff;
  --dot:#8fa6cf;
}
*{margin:0;padding:0;box-sizing:border-box}
html,body{width:1200px;height:3664px;overflow:hidden}
body{font-family:'Roboto',sans-serif;color:var(--ink);background:var(--white);position:relative}
.abs{position:absolute}
a{color:inherit;text-decoration:none}

.topbar{position:absolute;left:0;top:0;width:1200px;height:57px;background:var(--navy);color:var(--white)}
.topbar-links{position:absolute;right:146px;top:20px;font-size:12.5px;font-weight:700;letter-spacing:.1px}
.topbar-links span{margin:0 8px}
.topbar-search{position:absolute;left:1070px;top:20px}

.header{position:absolute;left:0;top:57px;width:1200px;height:102px;background:var(--light)}
.brand{position:absolute;left:109px;top:76px;display:flex;align-items:center;gap:10px}
.brand-mark{width:54px;height:54px;border-radius:50%;background:var(--navy)}
.brand-name{font-size:17px;font-weight:900;color:var(--navy);line-height:1.05}
.brand-name small{display:block;font-size:11px;font-weight:700}
.nav{position:absolute;right:112px;top:98px;display:flex;gap:33px;font-size:17.5px;font-weight:700;color:#111}

.hero{position:absolute;left:0;top:159px;width:1200px;height:586px;background:linear-gradient(100deg,#b8893f 0%,#c9a36a 18%,#8fa6b8 40%,#a9c0d4 60%,#b79a76 80%,#6f6a62 100%)}
.hero-shade{position:absolute;inset:0;background:linear-gradient(180deg,rgba(0,0,0,.05),rgba(0,0,0,.25))}
.hero-title{position:absolute;right:112px;top:125px;text-align:right;color:var(--white);font-weight:900;font-size:62px;line-height:62px}
.hero-sub{position:absolute;right:112px;top:270px;text-align:right;color:var(--white);font-weight:700;font-size:27px;line-height:34px}
.hero-btn{position:absolute;left:946px;top:361px;width:142px;height:46px;background:var(--navy);color:var(--white);font-weight:700;font-size:16.5px;display:flex;align-items:center;justify-content:center}
.hero-arrow{position:absolute;top:262px}
.hero-dots{position:absolute;left:996px;top:537px;display:flex;gap:14px}
.hero-dots i{width:12px;height:12px;border-radius:50%;background:rgba(255,255,255,.5)}
.hero-dots i:first-child{background:var(--white)}

.btn{display:inline-flex;align-items:center;justify-content:center;background:var(--navy);color:var(--white);font-weight:700;font-size:16.5px}

.about{position:absolute;left:0;top:745px;width:1200px;height:609px;background:var(--light)}
.about-photo{position:absolute;left:111px;top:85px;width:470px;height:438px;background:linear-gradient(160deg,#6e7379,#3a3d44 55%,#9aa0a6)}
.about-body{position:absolute;left:600px;top:82px;width:490px}
.about-body h2{font-size:24px;font-weight:700;margin-bottom:20px}
.about-body p{font-size:20px;line-height:27.6px;margin-bottom:21px}
.about-body .btn{width:142px;height:46px;margin-top:5px}

.engage{position:absolute;left:0;top:1354px;width:1200px;height:672px}
.section-title{position:absolute;left:0;width:1200px;text-align:center;font-weight:700;color:var(--navy-deep)}
.engage .section-title{top:82px;font-size:43px}
.card{position:absolute;top:160px;width:236px;text-align:center}
.card-photo{width:236px;height:140px;background:linear-gradient(135deg,#d9dde2,#9ba6b3)}
.card h3{font-size:22px;font-weight:700;color:var(--blue);line-height:26px;margin-top:12px;height:52px}
.card p{font-size:15px;line-height:22.3px;padding:0 10px;height:196px}
.card .btn{width:138px;height:41px;font-size:16.5px}

.events{position:absolute;left:0;top:2026px;width:1200px;height:597px;background:var(--light)}
.events .section-title{top:76px;font-size:25px;color:#111}
.event{position:absolute;top:155px;width:470px;height:359px;background:var(--white);box-shadow:0 1px 4px rgba(0,0,0,.15)}
.event h3{position:absolute;left:13px;top:29px;width:440px;font-size:19.5px;font-weight:700;line-height:25px}
.event-photo{position:absolute;left:13px;top:90px;width:139px;height:202px}
.event p{position:absolute;left:162px;top:86px;width:300px;font-size:17px;line-height:25.8px;color:#333}
.event .btn{position:absolute;left:0;bottom:0;width:470px;height:51px;font-size:16.5px}
.event-dots{position:absolute;left:558px;top:2578px;display:flex;gap:13px}
.event-dots i{width:11px;height:11px;border-radius:50%;background:var(--dot)}
.event-dots i:first-child{background:var(--blue)}

.investors{position:absolute;left:0;top:2623px;width:1200px;height:657px}
.investors .section-title{top:76px;font-size:43px}
.sponsor{position:absolute;display:flex;align-items:center;justify-content:center;gap:10px;font-weight:700;color:var(--navy);text-align:center;line-height:1.1}
.sponsor .mark{width:22px;height:22px;flex:none}

.footer{position:absolute;left:0;top:3280px;width:1200px;height:384px;background:var(--navy);color:var(--white);font-family:'Poppins',sans-serif}
.footer-brand{position:absolute;left:117px;top:92px;display:flex;align-items:center;gap:10px;opacity:.45}
.footer-brand .mark{width:52px;height:52px;border-radius:50%;background:#8aa0c8}
.footer-brand span{font-family:'Roboto',sans-serif;font-weight:900;font-size:18px;color:#c9d4ea;line-height:1.05}
.contact{position:absolute;left:117px;display:flex;gap:12px;font-size:15px;line-height:20px;font-weight:500}
.fcol{position:absolute;top:88px}
.fcol h4{font-size:19px;font-weight:500;margin-bottom:22px;letter-spacing:.3px}
.fcol li{list-style:none;font-size:15.5px;line-height:35.5px}
.footer-rule{position:absolute;left:0;top:336px;width:1200px;height:1px;background:rgba(255,255,255,.3)}
.copyright{position:absolute;left:113px;top:352px;font-size:12.5px}
.social{position:absolute;left:948px;top:351px;display:flex;gap:25px}
.social i{width:16px;height:16px;border-radius:50%;background:var(--white)}
</style>
</head>
<body>

<div class="topbar">
  <div class="topbar-links">ECONOMIC UPDATE<span>|</span>JOIN OUR EMAIL LIST<span>|</span>COMMUNITY INFO<span>|</span>RESOURCES + LINKS</div>
  <svg class="topbar-search" width="16" height="16" viewBox="0 0 16 16" fill="none" stroke="#fff" stroke-width="1.6"><circle cx="6.5" cy="6.5" r="5"/><line x1="10.2" y1="10.2" x2="15" y2="15"/></svg>
</div>

<header class="header"></header>
<div class="brand">
  <div class="brand-mark"></div>
  <div class="brand-name">GREATER VELMONT<small>CHAMBER OF COMMERCE</small></div>
</div>
<nav class="nav"><a>BUSINESS RESOURCES</a><a>PROGRAMS</a><a>MEMBERSHIP</a><a>EVENTS</a><a>CONTACT US</a></nav>

<section class="hero">
  <div class="hero-photo abs" style="inset:0" role="img" aria-label="Historic town square with ornate clock tower and grand civic buildings"></div>
  <div class="hero-shade"></div>
  <h1 class="hero-title">Greater Velmont<br>Chamber of Commerce</h1>
  <p class="hero-sub">To develop and promote an economically<br>vibrant business community.</p>
  <a class="hero-btn">LEARN MORE</a>
  <svg class="hero-arrow" style="left:54px" width="14" height="26" viewBox="0 0 14 26" fill="none" stroke="#fff" stroke-width="2"><polyline points="12,2 2,13 12,24"/></svg>
  <svg class="hero-arrow" style="left:1150px" width="14" height="26" viewBox="0 0 14 26" fill="none" stroke="#fff" stroke-width="2"><polyline points="2,2 12,13 2,24"/></svg>
  <div class="hero-dots"><i></i><i></i><i></i><i></i></div>
</section>

<section class="about">
  <div class="about-photo" role="img" aria-label="Members cutting a ribbon at a business grand opening with balloons"></div>
  <div class="about-body">
    <h2>ABOUT US</h2>
    <p>The mission of the Greater Velmont Chamber of Commerce is to aggressively develop and promote an economically vibrant business community.</p>
    <p>The Chamber, in both its values and practices, is committed to inclusion and excellence in the management of all diverse people irrespective of differences. This means that there shall be no barriers to participation in any activity of the Chamber on the basis of economic position, gender, race, creed, age, sexual orientation, gender identity, national origin, or disability.</p>
    <a class="btn">READ MORE</a>
  </div>
</section>

<section class="engage">
  <h2 class="section-title">ENGAGE TO THE VELMONT COMMERCE</h2>
  <div class="card" style="left:111px">
    <div class="card-photo" role="img" aria-label="Business advisor meeting a client at a desk"></div>
    <h3>BUSINESS<br>RESOURCES</h3>
    <p>We know times are challenging and we are here to help! See below for all of our resources and information to hopefully answer your questions on where to turn.</p>
    <a class="btn">READ MORE</a>
  </div>
  <div class="card" style="left:358px">
    <div class="card-photo" role="img" aria-label="Presenter leading a workshop around a conference table"></div>
    <h3>PROGRAMS</h3>
    <p>The Greater Velmont Chamber of Commerce has developed several programs that help our members succeed. Some programs are designed to directly help members.</p>
    <a class="btn">READ MORE</a>
  </div>
  <div class="card" style="left:606px">
    <div class="card-photo" role="img" aria-label="Hand signing a membership document with a pen"></div>
    <h3>MEMBERSHIP</h3>
    <p>The Greater Velmont Chamber of Commerce speaks for thousands of local business people. For over a hundred years, the Chamber has been the authoritative voice in all business matters.</p>
    <a class="btn">READ MORE</a>
  </div>
  <div class="card" style="left:853px">
    <div class="card-photo" role="img" aria-label="Professionals reviewing notes on a glass board"></div>
    <h3>HARBOR CALL</h3>
    <p>The Greater Velmont Chamber of Commerce is a powerful advocate for its members. The award winning Harbor Call is the voice of the Greater Velmont Chamber of Commerce and it is heard!</p>
    <a class="btn">READ MORE</a>
  </div>
</section>

<section class="events">
  <h2 class="section-title">EVENTS</h2>
  <article class="event" style="left:111px">
    <h3>WEBINAR 1/17/22 – 2023 LABOR LAW UPDATE</h3>
    <div class="event-photo" style="background:linear-gradient(135deg,#e7e2dc,#b9c4cf)" role="img" aria-label="Professional with a headset taking notes at a desk"></div>
    <p>2023 looks to be a bit brighter regarding the pandemic, but the Legislature refocused its attention on passing a multitude of labor and employment bills. This presentation will go over critical updates for California employers including New pay transparency requirements.</p>
    <a class="btn">LEARN MORE</a>
  </article>
  <article class="event" style="left:620px">
    <h3>JANUARY 5TH NETWORKING MIXER AT THE LINDELL THEATRE</h3>
    <div class="event-photo" style="background:linear-gradient(180deg,#d8b48a,#a3342e 60%,#6e1c1c)" role="img" aria-label="Historic theatre interior with red seats and balconies"></div>
    <p>This is your chance to kick-off the new year and enjoy the evening networking at Velmont's Crown jewel, with live music from Marla Quinn and the Copper Lanterns while meeting local professionals from the Greater Velmont Chamber. In addition, there will samples from Casa Rosalind's.</p>
    <a class="btn">LEARN MORE</a>
  </article>
</section>
<div class="event-dots"><i></i><i></i><i></i><i></i></div>

<section class="investors">
  <h2 class="section-title">THANKS TO OUR INVESTORS</h2>
  <div class="sponsor" style="left:120px;top:150px;width:180px;height:142px;font-size:17px"><span class="mark" style="background:var(--navy)"></span>LEADERSHIP<br>VELMONT</div>
  <div class="sponsor" style="left:345px;top:150px;width:230px;height:142px;font-size:20px;color:#3d4a3d">Verdant Valley<br>Partners</div>
  <div class="sponsor" style="left:612px;top:150px;width:210px;height:142px;font-size:19px;color:#111"><span class="mark" style="border-radius:50%;background:#1f7a3a"></span>Learning Works<br>Alliance</div>
  <div class="sponsor" style="left:862px;top:150px;width:200px;height:142px;font-size:19px;color:#7a2f2f">Policy Action<br>Council</div>
  <div class="sponsor" style="left:120px;top:313px;width:180px;height:256px;font-size:17px;color:#111"><span class="mark" style="background:#111"></span>Reuse<br>Enterprise Zone</div>
  <div class="sponsor" style="left:330px;top:313px;width:260px;height:256px;font-size:22px"><span class="mark" style="border-radius:50%;background:var(--navy)"></span>Connect<br>Circle</div>
  <div class="sponsor" style="left:594px;top:313px;width:248px;height:256px;font-size:18px">Velmont Chamber<br>Educational Series</div>
  <div class="sponsor" style="left:860px;top:313px;width:220px;height:256px;font-size:19px;color:#1f2a44"><span class="mark" style="border-radius:50%;background:#3a8a5c"></span>Common Ground<br>Initiative</div>
</section>

<footer class="footer">
  <div class="footer-brand"><div class="mark"></div><span>GREATER VELMONT<br>CHAMBER OF COMMERCE</span></div>
  <div class="contact" style="top:177px">
    <svg width="14" height="20" viewBox="0 0 14 20" fill="#fff"><path d="M7 0C3 0 0 3 0 7c0 5 7 13 7 13s7-8 7-13c0-4-3-7-7-7zm0 10a3 3 0 110-6 3 3 0 010 6z"/></svg>
    <span>120 Harbor Way, Suite 210<br>Velmont, California 95000</span>
  </div>
  <div class="contact" style="top:236px">
    <svg width="16" height="12" viewBox="0 0 16 12" fill="#fff" style="margin-top:4px"><path d="M0 0h16v12H0z"/><path d="M0 0l8 6 8-6" stroke="#1d3768" stroke-width="1.5" fill="none"/></svg>
    <span>info@velmontchamber.org</span>
  </div>
  <div class="contact" style="top:276px">
    <svg width="14" height="20" viewBox="0 0 14 20" fill="#fff"><path d="M3 0l3 5-2 2c1 3 3 6 6 8l2-2 2 4-3 3C5 19 0 11 1 2z"/></svg>
    <span>(555) 014-2770</span>
  </div>
  <div class="fcol" style="left:461px"><h4>QUCIK LINKS</h4><ul><li>Bussiness Resources</li><li>Programs</li><li>Membership</li><li>Events</li><li>Harbor Call</li></ul></div>
  <div class="fcol" style="left:711px;top:91px"><h4>INFORMATION</h4><ul><li>Service</li><li>Help &amp; Support</li><li>Privacy Policy</li><li>Terms &amp; Conditions</li><li>Site Map</li></ul></div>
  <div class="fcol" style="left:941px;top:90px"><h4>EXPLORE</h4><ul><li>Economic Update</li><li>Resources + Links</li><li>Community Info</li><li>Join Our Email List</li><li>Contact Us</li></ul></div>
  <div class="footer-rule"></div>
  <div class="copyright">Copyright Greater Velmont Chamber of Commerce 2022</div>
  <div class="social"><i></i><i></i><i></i><i></i></div>
</footer>

</body>
</html>
```